VerdaTurfix - 11" x 4" Door Hanger, full color both sides

We need a door hanger designed, 11" x 4", full color both sides, We are a lawn care company that provides lawn mowing, and other services to clients. This door hanger will be place on the 9 neighbors of our current clients. The ad needs to state that we provided lawn service to one of their neighbors today, and that we are in their neighborhood each week on that day. The door hanger will have 4 printings, substituting the day of Tuesday, Wednesday, Thursday, and Friday. All the art work and text will remain the same except the day of the week. For information about VerdaTurfix, please visit our website www.verdaturfix.net. The main emphasis of the message should be that we are their every week on that day, and the benefits to them of using our service (ie. quality time with their family, golf, sports, resting, etc., instead of mowing the lawn). At the bottom of the door hanger will be a coupon offering their tenth (10th) lawn service free, which is the same as a 10% discount.

I have uploaded a template files for the front and back of an 11 x 4 door hanger, The templates are pdf, jpeg, or eps files. The final product can be a pdf, jpeg, or eps file.

Target Market(s)

Neighbors of our existing clients

Industry/Entity Type

Lawn Care

Font styles to use
Serif

Requirements
Must have
• Professional design and art, Short conversational message that relays the following thoughts:
• 1. We mowed your neighbor's lawn today!
• 2. We are in your neighborhood every Tuesday!
• 3. Our lawn service is guaranteed.
• 4. Call to action - Call us today! 555-014-7382
• 5. Of course our contact info, name, phone number, website address.
• 6. Coupon at bottom for "10th lawn service Free!"
Nice to have
• Art work from our website is fine to use, That carries our theme throughout our campaign.
Should not have
• Very wordy. This is basically a billboard, Have very few seconds to grab their attention.

```html
<!DOCTYPE html>
<html lang="en">
<head>
<meta charset="utf-8">
<title>VerdaTurfix Door Hangers</title>
<link rel="stylesheet" href="https://fonts.googleapis.com/css2?family=Montserrat:wght@400&family=Oswald:wght@500;700&family=Lato:wght@400&display=swap">
<style>
  :root {
    --stage: #e8e8e8;
    --black: #151515;
    --red: #e2403d;
    --red-deep: #cf2f2d;
    --white: #ffffff;
    --yellow: #ffe94a;
    --badge-red: #e3242b;
    --green-light: #9fcb55;
    --green-dark: #3f7a2a;
  }
  * { margin: 0; padding: 0; box-sizing: border-box; }
  html, body { width: 1200px; height: 1042px; overflow: hidden; }
  body { background: var(--stage); position: relative; font-family: "Lato", sans-serif; }

  .hanger { position: absolute; top: 42px; width: 405px; height: 968px; background: var(--white); }
  .hanger--tuesday { left: 179px; }
  .hanger--today { left: 619px; top: 41px; }
  .hanger-art { position: absolute; inset: 0; width: 405px; height: 968px; display: block; }

  .brand { position: absolute; left: 0; width: 100%; text-align: center; font-family: "Montserrat", sans-serif; font-weight: 400; font-size: 32px; letter-spacing: 3px; color: var(--white); }

  .badge { position: absolute; text-align: center; font-family: "Oswald", sans-serif; line-height: 1.12; }
  .badge-line { display: block; color: var(--badge-red); font-weight: 700; }
  .badge-line--strong { color: var(--black); }

  .intro { position: absolute; left: 0; width: 100%; text-align: center; color: var(--white); font-size: 22px; }
  .headline { position: absolute; left: 0; width: 100%; text-align: center; color: var(--white); font-family: "Oswald", sans-serif; font-weight: 700; line-height: 1; }
  .rule { position: absolute; height: 2px; background: var(--white); }
  .call { position: absolute; left: 0; width: 100%; text-align: center; color: var(--yellow); font-family: "Oswald", sans-serif; font-weight: 500; font-size: 26px; line-height: 1; }
  .contact { position: absolute; left: 0; width: 100%; text-align: center; color: var(--yellow); font-size: 17px; line-height: 1; }

  .coupon { position: absolute; left: 0; width: 100%; text-align: center; font-family: "Oswald", sans-serif; font-weight: 500; color: var(--black); font-size: 26px; line-height: 1; white-space: nowrap; }
  .coupon-accent { color: var(--badge-red); }
  .coupon-big { font-size: 34px; }
</style>
</head>
<body>

<!-- Tuesday hanger -->
<section class="hanger hanger--tuesday">
  <svg class="hanger-art" viewBox="0 0 405 968" aria-hidden="false">
    <defs>
      <linearGradient id="photoMowing" x1="0" y1="0" x2="0" y2="1">
        <stop offset="0" stop-color="#2f6b22"/>
        <stop offset="0.55" stop-color="#5d9b35"/>
        <stop offset="1" stop-color="#9fcb55"/>
      </linearGradient>
      <linearGradient id="redBody" x1="0" y1="0" x2="0" y2="1">
        <stop offset="0" stop-color="#e03c39"/>
        <stop offset="1" stop-color="#d83532"/>
      </linearGradient>
    </defs>
    <rect x="0" y="100" width="405" height="480" fill="url(#photoMowing)" role="img" aria-label="Photo of a lawn worker pushing a green mower across a garden lawn"/>
    <path d="M0,160 C70,180 130,185 200,170 C280,150 330,122 405,122 V0 H0 Z" fill="var(--red)"/>
    <path d="M0,150 C70,170 130,175 200,160 C280,140 330,112 405,112 V0 H0 Z" fill="var(--black)"/>
    <path d="M0,546 C80,532 160,548 240,588 C300,618 360,628 405,618 V968 H0 Z" fill="var(--white)"/>
    <path d="M0,560 C80,545 160,560 240,600 C300,630 360,640 405,630 V968 H0 Z" fill="url(#redBody)"/>
    <path d="M230,590 C300,625 360,632 405,622 V642 C350,650 290,640 230,590 Z" fill="var(--black)"/>
    <circle cx="202" cy="175" r="62" fill="var(--white)"/>
    <circle cx="306" cy="559" r="86" fill="#f3c9c6" opacity="0.75"/>
    <circle cx="306" cy="559" r="79" fill="var(--badge-red)"/>
    <circle cx="306" cy="559" r="73" fill="var(--black)"/>
    <circle cx="306" cy="559" r="69" fill="var(--white)"/>
    <rect x="0" y="850" width="405" height="118" fill="var(--white)"/>
    <line x1="0" y1="850" x2="405" y2="850" stroke="var(--red)" stroke-width="2" stroke-dasharray="4 3"/>
    <g class="scissors" stroke="var(--black)" stroke-width="1.4" fill="none">
      <circle cx="45" cy="841" r="2.5"/><circle cx="45" cy="849" r="2.5"/>
      <line x1="47" y1="842" x2="62" y2="849"/><line x1="47" y1="848" x2="62" y2="841"/>
    </g>
  </svg>
  <div class="brand" style="top:50px;">VERDATURFIX</div>
  <div class="badge" style="left:236px; top:503px; width:140px;">
    <span class="badge-line" style="font-size:26px;">Lawn</span>
    <span class="badge-line" style="font-size:22px;">Service is</span>
    <span class="badge-line badge-line--strong" style="font-size:23px;">GUARANTEED</span>
  </div>
  <div class="intro" style="top:660px;">We are in your neighborhood</div>
  <div class="headline" style="top:690px; font-size:48px;">EVERY TUESDAY!</div>
  <div class="rule" style="left:56px; width:296px; top:750px;"></div>
  <div class="call" style="top:760px;">Call us today! 555-014-7382</div>
  <div class="contact" style="top:795px;">EMAIL: service@verdaturfix.net</div>
  <div class="contact" style="top:818px;">www.verdaturfix.net</div>
  <div class="coupon" style="top:872px;"><span class="coupon-accent coupon-big">10TH</span> LAWN SERVICE <span class="coupon-accent">FREE!</span></div>
</section>

<!-- Lawn today hanger -->
<section class="hanger hanger--today">
  <svg class="hanger-art" viewBox="0 0 405 968">
    <defs>
      <linearGradient id="photoBlower" x1="0" y1="0" x2="0" y2="1">
        <stop offset="0" stop-color="#3d7a28"/>
        <stop offset="0.5" stop-color="#7fb43f"/>
        <stop offset="1" stop-color="#a8d35c"/>
      </linearGradient>
      <linearGradient id="redBody2" x1="0" y1="0" x2="0" y2="1">
        <stop offset="0" stop-color="#e03c39"/>
        <stop offset="1" stop-color="#d83532"/>
      </linearGradient>
    </defs>
    <rect x="0" y="100" width="405" height="460" fill="url(#photoBlower)" role="img" aria-label="Photo of a lawn worker clearing freshly cut striped grass with a leaf blower"/>
    <path d="M0,170 C70,190 130,192 200,175 C280,155 330,132 405,132 V0 H0 Z" fill="var(--red)"/>
    <path d="M0,160 C70,180 130,182 200,165 C280,145 330,122 405,122 V0 H0 Z" fill="var(--black)"/>
    <path d="M0,530 C60,545 120,545 200,502 C280,452 340,350 405,343 V968 H0 Z" fill="var(--black)"/>
    <path d="M0,538 C60,553 120,553 200,511 C280,462 340,368 405,362 V968 H0 Z" fill="var(--white)"/>
    <path d="M0,548 C60,563 120,563 200,521 C280,472 340,385 405,378 V968 H0 Z" fill="url(#redBody2)"/>
    <circle cx="202" cy="174" r="62" fill="var(--white)"/>
    <circle cx="201" cy="511" r="94" fill="#f3c9c6" opacity="0.75"/>
    <circle cx="201" cy="511" r="87" fill="var(--badge-red)"/>
    <circle cx="201" cy="511" r="81" fill="var(--black)"/>
    <circle cx="201" cy="511" r="73" fill="var(--white)"/>
    <rect x="0" y="849" width="405" height="119" fill="var(--white)"/>
    <line x1="0" y1="849" x2="405" y2="849" stroke="var(--red)" stroke-width="2" stroke-dasharray="4 3"/>
    <g class="scissors" stroke="var(--black)" stroke-width="1.4" fill="none">
      <circle cx="45" cy="840" r="2.5"/><circle cx="45" cy="848" r="2.5"/>
      <line x1="47" y1="841" x2="62" y2="848"/><line x1="47" y1="847" x2="62" y2="840"/>
    </g>
  </svg>
  <div class="brand" style="top:59px;">VERDATURFIX</div>
  <div class="badge" style="left:121px; top:447px; width:160px;">
    <span class="badge-line" style="font-size:31px;">Lawn</span>
    <span class="badge-line" style="font-size:26px;">Service is</span>
    <span class="badge-line badge-line--strong" style="font-size:27px;">GUARANTEED</span>
  </div>
  <div class="intro" style="top:629px;">We mowed your neighbor's</div>
  <div class="headline" style="top:667px; font-size:56px;">LAWN TODAY!</div>
  <div class="rule" style="left:55px; width:295px; top:734px;"></div>
  <div class="call" style="top:744px;">Call us today! 555-014-7382</div>
  <div class="contact" style="top:779px;">EMAIL: service@verdaturfix.net</div>
  <div class="contact" style="top:803px;">www.verdaturfix.net</div>
  <div class="coupon" style="top:871px;"><span class="coupon-accent coupon-big">10TH</span> LAWN SERVICE <span class="coupon-accent">FREE!</span></div>
</section>

</body>
</html>
```